Postcard for our major fundraising event - LiftingDAWN2018

Bright Meadow YOUTH Camp (BMY) and Youth Summit Trail Camp (YSTC) are ministries of Larkwell Fellowship Church that serve Ventura County children of abuse, abandonment and neglect living in foster care. We are looking for a postcard design to promote our single largest fundraising event of the year, NurturingDAWN2018, to raise awareness and support for children of abuse. NurturingDAWN is a dinner banquet on at an exclusive outdoor venue, "Willow Hollow" with a rustic, ranch feel and with spectacular panoramic views of the City of Camarillo. The event will include music, refreshments, appetizers, a Santa Maria-style barbeque (BBQ), coffee and dessert, testimonials from camp, prize drawings, an opportunity to partner with BMY and YSTC, and time to socialize before and after.
Updates

I have just uploaded text copy to help designers come closer to what we are looking for. Thank you very much for your interest! -Dale

Target Market(s)

People from both within and from outside our sponsoring church who have a heart for hurting children and who are willing and able to financially support our camping (BMY & YSTC) ministries.

Industry/Entity Type

Church

Font styles to use
Serif
Decorative
Script

Requirements
Must have
• Name: NurturingDAWN2018... raising awareness and support for children of abuse
• Date: Thursday, May 24, 2018, 6:30-8:00 pm
• Place: Willow Hollow at Harlow Spread, 2715 Calder Lane, Somis, California.
• Cost: $30 per person
• Tickets: Available at Tixmoor.com
• Front side should include the elements of the event (although not necessarily bulleted like below):
• • Social hour
• • Music
• • Hors d’eourves
• • Refreshments
• • Santa Maria-style BBQ dinner
• • Coffee & dessert
• • Prize drawings
• • Stories from camp
• See attachment for suggested copy for back side.
• BMY and YSTC logos should be included on the postcard. I’ve uploaded a variety of photos for the designer to choose from; they do not necessarily all have to be included. There are also lots more pics available on our Pagebook (Bright Meadow YOUTH of Ventura).
• The front-side of the postcard can be entirely images and text. The back-side of the post card should include our return address at the top left ("BMY/YSTC of Larkwell Fellowship Church, 812 Fernbrook Court, Ventura, CA 93871") and should leave at least the right half of the postcard clear for addressing and postage.
• BMY colors are purple (Pantone 267) and red (Pantone 186). YSTC colors are green and yellow.
Nice to have
• A selection of camp photos large enough to easily view, but no so many that they are too small to identify. And, perhaps, a design element that evokes a rustic, outdoors, western, ranch feel, but not so much that it seems that we are promoting a country hoedown.
Should not have
• Anything sexual or sensual, related to alcoholic beverages, gambling, guns, or anything negative.

```html
<!DOCTYPE html>
<html lang="en">
<head>
<meta charset="utf-8">
<title>NurturingDAWN2018 Postcard</title>
<link rel="stylesheet" href="https://fonts.googleapis.com/css2?family=Rye&family=Kalam:wght@700&family=Lato:ital,wght@0,400;0,700;0,900;1,400;1,700;1,900&display=swap">
<style>
  :root {
    --bg: #555555;
    --red: #d71f2b;
    --green: #17a24a;
    --yellow: #f4e43c;
    --gold: #f7d417;
    --purple: #5b2c86;
    --ink: #333333;
    --white: #ffffff;
    --rule: #9a9a9a;
  }
  html, body { margin: 0; padding: 0; overflow: hidden; }
  body {
    width: 1200px; height: 2663px;
    background: var(--bg);
    position: relative;
    font-family: "Lato", Arial, sans-serif;
  }
  .card {
    position: absolute;
    left: 69px;
    width: 1062px;
    background: var(--white);
    overflow: hidden;
  }
  .card-front { top: 615px; height: 680px; }
  .card-back { top: 1415px; height: 632px; }
  .card svg.shapes { position: absolute; left: 0; top: 0; }

  .event-title {
    position: absolute; left: 48px; top: 22px; margin: 0;
    font-family: "Rye", Georgia, serif; font-weight: 400;
    font-size: 52px; color: var(--yellow); letter-spacing: 1px;
    line-height: 1; white-space: nowrap;
  }
  .event-tagline {
    position: absolute; left: 48px; top: 100px; margin: 0;
    font-style: italic; font-weight: 700; font-size: 27px; color: var(--white);
    white-space: nowrap;
  }
  .event-date {
    position: absolute; left: 52px; top: 168px; margin: 0;
    font-family: "Kalam", cursive; font-weight: 700; font-size: 40px; line-height: 48px;
  }
  .event-date .day { color: var(--red); display: block; }
  .event-date .date { color: var(--purple); display: block; }
  .event-date .time { color: var(--green); display: block; }
  .event-venue {
    position: absolute; left: 52px; top: 330px; margin: 0;
    font-style: italic; font-size: 21px; line-height: 28px; color: var(--ink);
  }
  .event-venue svg { position: absolute; left: -34px; top: 4px; }
  .event-cost {
    position: absolute; left: 60px; top: 432px; margin: 0;
    font-style: italic; font-weight: 900; font-size: 30px; color: var(--white);
  }
  .event-tickets {
    position: absolute; left: 60px; top: 474px; margin: 0;
    font-size: 21px; color: var(--white);
  }
  .brand {
    position: absolute; display: flex; align-items: center; gap: 10px;
    font-weight: 900; font-size: 26px; line-height: 1.05;
  }
  .brand-mark { width: 26px; height: 26px; border-radius: 50%; flex: none; }
  .brand-bmy { color: var(--purple); }
  .brand-bmy .brand-mark { background: var(--red); }
  .brand-ystc { color: var(--green); }
  .brand-ystc .brand-mark { background: var(--gold); }
  .card-front .brand-bmy { left: 66px; top: 570px; }
  .card-front .brand-ystc { left: 318px; top: 584px; }
  .card-back .brand-bmy { left: 46px; top: 40px; }
  .card-back .brand-ystc { left: 298px; top: 54px; }

  .return-address {
    position: absolute; left: 590px; top: 26px; margin: 0; width: 262px;
    font-size: 17px; line-height: 22px; color: var(--ink); font-style: normal;
  }
  .stamp-box {
    position: absolute; left: 877px; top: 28px; width: 152px; height: 150px;
    border: 1.5px solid var(--rule); box-sizing: border-box;
  }
  .address-line {
    position: absolute; left: 690px; width: 341px; height: 0;
    border-top: 1.5px solid var(--rule);
  }
</style>
</head>
<body>

<section class="card card-front" aria-label="Postcard front">
  <svg class="shapes" width="1062" height="680" viewBox="0 0 1062 680">
    <defs>
      <linearGradient id="venuePhoto" x1="0" y1="0" x2="1" y2="1">
        <stop offset="0" stop-color="#e7dc5a"/>
        <stop offset="0.5" stop-color="#c9bd3c"/>
        <stop offset="1" stop-color="#8f8a2e"/>
      </linearGradient>
      <linearGradient id="crowdPhoto" x1="0" y1="0" x2="0" y2="1">
        <stop offset="0" stop-color="#7aa6c9"/>
        <stop offset="1" stop-color="#8c7a64"/>
      </linearGradient>
      <linearGradient id="rallyPhoto" x1="0" y1="0" x2="0" y2="1">
        <stop offset="0" stop-color="#4f7fd0"/>
        <stop offset="1" stop-color="#b8322f"/>
      </linearGradient>
      <linearGradient id="buffetPhoto" x1="0" y1="0" x2="1" y2="1">
        <stop offset="0" stop-color="#c9c1a8"/>
        <stop offset="1" stop-color="#4f7a3a"/>
      </linearGradient>
      <linearGradient id="footerSwoosh" x1="0" y1="0" x2="0" y2="1">
        <stop offset="0" stop-color="#ffffff"/>
        <stop offset="1" stop-color="#e4e4e4"/>
      </linearGradient>
    </defs>
    <rect x="0" y="142" width="1062" height="381" fill="url(#venuePhoto)" role="img" aria-label="Photo of the outdoor ranch venue under trees"/>
    <polygon points="0,142 250,142 440,332 250,523 0,523" fill="#ffffff" fill-opacity="0.88"/>
    <rect x="0" y="523" width="1062" height="157" fill="url(#footerSwoosh)"/>
    <path d="M0,560 C300,520 600,600 1062,540 L1062,560 C600,620 300,545 0,585 Z" fill="#efefef"/>
    <polygon points="873,0 1062,0 1062,186" fill="var(--green)"/>
    <polygon points="0,0 873,0 1000,142 0,142" fill="var(--red)"/>
    <polygon points="568,112 740,284 568,456 396,284" fill="url(#crowdPhoto)" stroke="#fff" stroke-width="4" role="img" aria-label="Photo of camp volunteers holding welcome signs"/>
    <polygon points="905,118 1075,288 905,458 735,288" fill="url(#rallyPhoto)" stroke="#fff" stroke-width="4" role="img" aria-label="Photo of a crowd in red shirts waving signs"/>
    <polygon points="728,290 894,456 728,622 562,456" fill="url(#buffetPhoto)" stroke="#fff" stroke-width="4" role="img" aria-label="Photo of guests at a banquet buffet table"/>
    <polygon points="745,180 805,240 745,300 685,240" fill="var(--red)"/>
    <polygon points="0,417 465,417 440,461 465,506 0,506" fill="var(--red)"/>
  </svg>

  <h1 class="event-title">NurturingDAWN2018...</h1>
  <p class="event-tagline">Raising awareness and support for children of abuse</p>
  <p class="event-date">
    <span class="day">Thursday,</span>
    <span class="date">May 24, 2018,</span>
    <span class="time">6:30-8:00 pm</span>
  </p>
  <p class="event-venue">
    <svg width="18" height="24" viewBox="0 0 18 24" aria-hidden="true"><path d="M9,0 C4,0 0,4 0,9 C0,15 9,24 9,24 C9,24 18,15 18,9 C18,4 14,0 9,0 Z" fill="var(--red)"/><circle cx="9" cy="9" r="3.5" fill="#fff"/></svg>
    Willow Hollow at Harlow Spread<br>2715 Calder Lane,<br>Somis, California
  </p>
  <p class="event-cost">Cost: $30 per person</p>
  <p class="event-tickets">Tickets: Available at Tixmoor.com</p>

  <div class="brand brand-bmy"><span class="brand-mark"></span><span>Bright Meadow<br>YOUTH</span></div>
  <div class="brand brand-ystc"><span class="brand-mark"></span><span>YSTC</span></div>
</section>

<section class="card card-back" aria-label="Postcard back">
  <svg class="shapes" width="1062" height="632" viewBox="0 0 1062 632">
    <defs>
      <linearGradient id="ziplinePhoto" x1="0" y1="0" x2="0" y2="1">
        <stop offset="0" stop-color="#3f7fd6"/>
        <stop offset="0.65" stop-color="#a9c8e8"/>
        <stop offset="1" stop-color="#3d5a2c"/>
      </linearGradient>
    </defs>
    <polygon points="0,156 530,156 460,591 0,591" fill="url(#ziplinePhoto)" role="img" aria-label="Photo of campers riding a zip line above pine trees"/>
    <polygon points="555,0 585,0 490,591 460,591" fill="var(--red)"/>
  </svg>

  <div class="brand brand-bmy"><span class="brand-mark"></span><span>Bright Meadow<br>YOUTH</span></div>
  <div class="brand brand-ystc"><span class="brand-mark"></span><span>YSTC</span></div>

  <address class="return-address">BMY/YSTC of Larkwell Fellowship Church, 812 Fernbrook Court, Ventura, CA 93871</address>
  <div class="stamp-box"></div>
  <div class="address-line" style="top:248px"></div>
  <div class="address-line" style="top:298px"></div>
  <div class="address-line" style="top:343px"></div>
  <div class="address-line" style="top:389px"></div>
</section>

</body>
</html>
```